Personal coach needs brochure design for inspirational essay about authenticity

Overview:
I want a beautiful brochure, 11”x17” that folds to 8-1/2”x11” with 4 pages. Think of it as an oversize greeting card.
• Front cover: photograph of a dancer and title with attribution of quote (Lumafold jpeg photo attached)
• Inside spread: Copy (Helena Brisk copy attached) with some appropriate illustration, based on cover photo
• Back cover: contact information, brief descriptive copy, two small photos (jpeg photo attached; see copy for direction)
Copy for front cover title, inside spread and back cover is attached in doc titled "Helena Brisk copy"

Purpose of brochure:
I'm a personal coach and once a year I produce a 4-page illustrated inspirational essay, which invites personal reflection on living a more mindful, meaningful life. Most people I send them to collect them. Someday in the future I'd like to put a collection of these essays into a coffee table book and also create a website for the collection, which is related to the personal coaching that I do.
I have the brochures printed hard copy. I have attached a few examples from previous years. Each has a unique design related to its theme.

Concept:
This year’s essay theme, “There will only ever be one you!” is based on a quote by Helena Brisk, a famous modern dancer. The complete quote, which appears in the copy, is about being true to one’s authentic self. The essay is not about dance, but because the author of the quote was a dancer who personified this theme of being unique to self, I have selected a photo of dance for the cover.

Design Guidance:
Front cover: One possibility is to expand the background color of the Lumafold photo so the photo seems to emerge from the background. But I am open to ideas. I think the photo is artsy enough as it is, but there may be other ways to treat it (e.g. special effects) that would also work. The title should appear somewhere. Make the attribution (--Helena Brisk) in smaller type than the title.

Inside Spread: There may be ways to borrow a design motif from the cover photo to make the inside spread more visually interesting, i.e., not just straight copy. I think it may be helpful to make the font size of the quote larger than the rest of the copy, but it has to be read in sequence. Or maybe it's printed in same size as copy, but then also repeated and displayed by itself in larger type.

Back cover: If you look at some of the other examples I’ve sent, you’ll see how the back cover is typically handled. I want a reduced version of the cover to be placed near the line that says "this is the 16th in a series.." Then, there’s a jpeg photo of Helena Brisk that should be placed next to the copy description of her.

Need extra days to review

```html
<!DOCTYPE html>
<html lang="en">
<head>
<meta charset="utf-8">
<title>There Will Only Ever Be One You! – Brochure</title>
<link href="https://fonts.googleapis.com/css2?family=Cinzel:wght@400;600&family=Poppins:ital,wght@0,300;0,400;0,600;0,700;1,400&display=swap" rel="stylesheet">
<style>
  :root{
    --canvas:#e5e5e5;
    --paper:#141414;
    --paper-deep:#0b0b0b;
    --ink:#f2f2f2;
    --ink-soft:#d6d6d6;
    --rule:#8a8a8a;
    --pill:#cfcfcf;
    --pill-ink:#1a1a1a;
    --quote-box:#4b4b4b;
    --smoke:#5a5a5a;
    --dress:#3b4a5e;
  }
  *{box-sizing:border-box;margin:0;padding:0}
  html,body{width:1200px;height:2475px;overflow:hidden}
  body{background:var(--canvas);font-family:'Poppins',sans-serif;color:var(--ink);position:relative}

  .spread{position:absolute;left:50px;width:1100px;height:712px;background:var(--paper);
    box-shadow:0 6px 18px rgba(0,0,0,.35);overflow:hidden}
  .spread--outside{top:485px;background:linear-gradient(90deg,var(--paper-deep) 0%,#161616 48%,#1a1a1a 50%,#0e0e0e 100%)}
  .spread--inside{top:1277px;background:radial-gradient(ellipse at 25% 30%,#232323 0%,var(--paper-deep) 70%)}
  .abs{position:absolute}

  /* back cover */
  .mini-cover{left:52px;top:52px;width:107px;height:151px;border:2px solid var(--ink);
    background:radial-gradient(ellipse at 50% 60%,#4a4f57 0%,#1b1b1b 75%);text-align:center;padding-top:7px}
  .mini-cover__line1{font-family:'Cinzel',serif;font-size:7px;color:var(--ink-soft)}
  .mini-cover__line2{font-family:'Cinzel',serif;font-size:12px;font-weight:600;line-height:13px}
  .mini-cover__name{position:absolute;bottom:7px;left:0;right:0;font-size:5.5px;letter-spacing:1.5px}
  .series{left:178px;top:48px;width:350px}
  .series__title{font-size:14.5px;font-weight:700;text-transform:uppercase;line-height:18.5px}
  .series__intro{font-size:13.5px;font-weight:300;line-height:16px;margin-top:2px}
  .series__contact{font-size:12.5px;line-height:17px;margin-top:20px}
  .series__contact strong{font-weight:600}
  .pills{left:52px;top:240px;display:flex;gap:18px}
  .pill{display:flex;align-items:center;gap:5px}
  .pill__icon{width:20px;height:20px}
  .pill__text{background:var(--pill);color:var(--pill-ink);font-size:12px;font-weight:600;padding:1px 8px;line-height:16px}
  .divider{left:52px;top:302px;width:458px;height:1px;background:var(--rule)}
  .divider-mark{left:255px;top:294px;width:66px;height:16px;background:#7a7a7a;border-radius:8px}
  .quote-credit{left:85px;top:330px;width:430px}
  .quote-mark{font-family:Georgia,serif;font-size:44px;font-weight:700;line-height:1;color:var(--ink-soft)}
  .quote-credit .quote-mark--open{position:absolute;left:0;top:-2px}
  .quote-credit .quote-mark--close{position:absolute;left:340px;top:26px}
  .quote-credit__text{margin-left:45px;font-size:14.5px;font-weight:600;line-height:18.5px}
  .portrait{left:52px;top:410px;width:106px;height:127px;border:2px solid var(--ink);
    background:radial-gradient(ellipse at 50% 60%,#8d857a 0%,#3a3835 55%,#1c1c1c 100%)}
  .about{left:171px;top:402px;width:346px}
  .about__title,.photog__title{font-size:13px;font-weight:600;line-height:17px}
  .about__body,.photog__body{font-size:8.8px;font-weight:300;line-height:10.8px;color:var(--ink-soft)}
  .photog{left:52px;top:558px;width:462px}

  /* front cover */
  .cover-photo{left:550px;top:0;width:550px;height:712px;
    background:radial-gradient(ellipse at 55% 52%,var(--smoke) 0%,#3a3a3a 28%,#1e1e1e 58%,#0f0f0f 100%)}
  .cover-figure{left:640px;top:190px;width:420px;height:400px;border-radius:46% 40% 50% 44%;
    background:radial-gradient(ellipse at 55% 50%,var(--dress) 0%,#2c3744 45%,rgba(40,44,52,0) 72%)}
  .cover-title{left:560px;top:50px;width:530px;text-align:center;font-family:'Cinzel',serif}
  .cover-title__lead{font-size:37px;line-height:42px}
  .cover-title__main{font-size:66px;font-weight:600;line-height:70px;margin-top:4px;
    color:#ececec}
  .cover-name{left:560px;top:628px;width:530px;text-align:center;font-size:29px;letter-spacing:9px;font-weight:400}

  /* inside spread */
  .essay{font-size:11.5px;line-height:12.9px;font-weight:400;color:var(--ink-soft)}
  .essay strong{font-weight:700;color:var(--ink)}
  .photo-leap{left:50px;top:55px;width:205px;height:430px;
    background:radial-gradient(ellipse at 50% 45%,#5c5c5c 0%,#2a2a2a 40%,rgba(20,20,20,0) 72%)}
  .photo-kneel{left:775px;top:335px;width:325px;height:377px;
    background:radial-gradient(ellipse at 60% 55%,#5e5e5e 0%,#2f2f2f 42%,rgba(14,14,14,0) 75%)}
  .p1{left:256px;top:54px;width:255px}
  .p2{left:256px;top:282px;width:255px}
  .p3{left:56px;top:462px;width:456px}
  .p4{left:52px;top:582px;width:462px}
  .lead-in{left:590px;top:55px;font-size:12px}
  .pull-quote{left:589px;top:81px;width:461px;height:262px;background:var(--quote-box);
    padding:14px 16px 0;text-align:center;font-size:15.3px;line-height:19.4px;color:var(--ink)}
  .pull-quote .quote-mark--open{position:absolute;left:12px;top:6px;font-size:46px}
  .pull-quote .quote-mark--close{position:absolute;right:62px;bottom:4px;font-size:46px}
  .pull-quote__text{padding-top:22px}
  .p5{left:590px;top:383px;width:185px}
  .p6{left:590px;top:515px;width:185px}
</style>
</head>
<body>

<section class="spread spread--outside" aria-label="Outside spread: back cover and front cover">
  <div class="abs mini-cover" aria-label="Reduced front cover">
    <div class="mini-cover__line1">THERE WILL ONLY EVER</div>
    <div class="mini-cover__line2">BE ONE YOU!</div>
    <div class="mini-cover__name">HELENA BRISK</div>
  </div>

  <div class="abs series">
    <h2 class="series__title">There will only ever be one you is<br>the 16th in a series of Labor Day essays</h2>
    <p class="series__intro">inviting a moment of reflection on living a more meaningful, more mindful life</p>
    <p class="series__contact"><strong>Lena Marsh Holloway, Ph.D.</strong><br>Heron Hill House<br>18 Orchard Lane<br>Fairhaven, Vermont&nbsp; 05743</p>
  </div>

  <div class="abs pills">
    <div class="pill">
      <svg class="pill__icon" viewBox="0 0 20 20"><circle cx="10" cy="10" r="9" fill="none" stroke="#f2f2f2" stroke-width="1.5"/><path d="M6.5 5.5l2 0 1 2.5-1.3 1a6 6 0 0 0 2.8 2.8l1-1.3 2.5 1v2c0 .6-.5 1-1 1A8 8 0 0 1 5.5 6.5c0-.5.4-1 1-1z" fill="#f2f2f2"/></svg>
      <span class="pill__text">555-214-3098</span>
    </div>
    <div class="pill">
      <svg class="pill__icon" viewBox="0 0 20 20"><circle cx="10" cy="10" r="9" fill="none" stroke="#f2f2f2" stroke-width="1.5"/><rect x="5" y="6.5" width="10" height="7" fill="none" stroke="#f2f2f2" stroke-width="1.3"/><path d="M5 6.8l5 4 5-4" fill="none" stroke="#f2f2f2" stroke-width="1.3"/></svg>
      <span class="pill__text">lholloway@northmail.net</span>
    </div>
  </div>

  <div class="abs divider"></div>
  <div class="abs divider-mark" role="img" aria-label="Small decorative flourish centred on the rule"></div>

  <div class="abs quote-credit">
    <span class="quote-mark quote-mark--open">&ldquo;</span>
    <p class="quote-credit__text">Helena Brisk in Letter to the World,<br>No. 1&rdquo;&nbsp; &copy; The Clara Weston Archive</p>
    <span class="quote-mark quote-mark--close">&rdquo;</span>
  </div>

  <div class="abs portrait" role="img" aria-label="Black and white photograph of Helena Brisk dancing in a flowing skirt"></div>
  <div class="abs about">
    <h3 class="about__title">About Helena Brisk</h3>
    <p class="about__body">Born in 1894, Helena Brisk danced and taught for over 70 years.&nbsp; She is recognized as a primal artistic force of the 20th century, whose influence on modernity has been compared to Aurel Vance, Tomas Reid, Ilya Marek, and Owen Pratt.&nbsp; Her themes dealt with the lives and conflicts of ordinary people, and she brought serious issues to the stage like war, poverty, intolerance and the injustices of slavery and treatment of Native Americans. Rebelling against conventions of the past, her dancing and choreography exposed the depths of human emotion through intense movements that were forceful, stark, angular, jagged, and percussive – startlingly unlike the formality of classical ballet, which she saw as antiquated.</p>
  </div>
  <div class="abs photog">
    <h3 class="photog__title">About Photographer Clara Weston</h3>
    <p class="photog__body">In 1935 Clara Weston saw a performance by modern dancer and choreographer Helena Brisk. Weston was so inspired by the dance performance that she introduced herself to Brisk, and the two artists began an artistic collaboration that lasted more than 60 years. Weston often photographed dancers in action, to capture the emotion behind their movement. Her artistic style was in line with Brisk’s philosophy of dance. This photo from the dance, “Letter to the World,” is one of Weston’s most famous photographs. The title of this work comes from an Edith Hale poem, which inspired Brisk to create a dance performance based on Hale’s life.</p>
  </div>

  <div class="abs cover-photo" role="img" aria-label="Photograph of a dancer in a flowing blue-grey dress leaping mid-air against dark smoke"></div>
  <div class="abs cover-figure" aria-hidden="true"></div>
  <h1 class="abs cover-title">
    <span class="cover-title__lead" style="display:block">THERE WILL ONLY EVER</span>
    <span class="cover-title__main" style="display:block">BE ONE YOU!</span>
  </h1>
  <p class="abs cover-name">HELENA BRISK</p>
</section>

<section class="spread spread--inside" aria-label="Inside spread: essay">
  <div class="abs photo-leap" role="img" aria-label="Black and white photograph of a ballerina in a tutu on pointe, arm raised, in drifting dust"></div>

  <p class="abs essay p1">In the rural Ohio village where I grew up, one of the highlights of Sunday morning church service -- in between congregational hymn-singing and the preacher’s sermon -- was the “special selection,” a musical performance by a parishioner. Typically, it was a vocalist or instrumental on piano, organ or violin.&nbsp; One Sunday, we were surprised by an unusual performance.&nbsp; A plump, buxom farm wife approached the pulpit, puckered up her lips and unexpectedly began to whistle the hymn “The Old Rugged Cross.” As a 10-year-old, I found this hilarious as I tried to choke back my wide-eyed amazement and giggles.</p>

  <p class="abs essay p2">Despite the irreverence of my pre-adolescent reaction, this memory has stayed with me for decades as an iconic example of the wonderment of individual differences. Of the delight I find in witnessing someone express herself in sometimes surprising and even courageous ways.&nbsp; Of the marvel of beholding a person be truly authentic and uniquely original.</p>

  <p class="abs essay p3">Someone who personified the irrepressible impulse to express her individuality was the early 20th century dancer and choreographer Helena Brisk.&nbsp; A pioneer of modern dance, she&nbsp; threw tradition overboard and was inspired to dance in a way that was a radical departure from the formalized style and rigidly dictated forms of classical ballet. Brisk felt compelled to express the rawness and emotion of human experience in her dancing -- not just present a form of pretty entertainment. Iconoclastically brilliant, she created a new language of dance, a revolutionary vocabulary of movement that electrified the stage, often creating a visceral response in the audience</p>

  <p class="abs essay p4">In her biography of Brisk, her friend and equally talented choreographer Ruth Calder recalled that despite sensational reviews for her own innovative work in the Broadway musical Prairie Song, Calder had a gnawing feeling that her work was only mediocre.&nbsp; Calder confessed her anxieties to Brisk who listened quietly and then responded, <strong>“There will only ever be one you!”</strong></p>

  <p class="abs lead-in">Continuing, she added:</p>
  <blockquote class="abs pull-quote">
    <span class="quote-mark quote-mark--open">&ldquo;</span>
    <p class="pull-quote__text">There is a vitality, a life-force, an energy, a quickening that is translated through you into action. And because there is only one of you in all of time, this expression is unique.&nbsp; And if you block it, the world will not have it. It is not your business to determine how good it is nor how valuable nor how it compares with other expressions. It is your business to keep it yours clearly and directly, to keep the channel open. You have to keep open and aware directly to the urges that motivate you.&nbsp; Above all else, keep the channel open</p>
    <span class="quote-mark quote-mark--close">&rdquo;</span>
  </blockquote>

  <p class="abs essay p5">Brisk’s wisdom reminds us that we must not hold back or judge our gifts.&nbsp; Although there may be moments when we doubt ourselves or when we worry that we’re not good enough, our job is to be fearless and to “keep the channel open.”</p>

  <p class="abs essay p6">Guard the precious miracle of your own uniqueness.&nbsp; Find that home-sweet-home feeling where you feel you are your most authentic self.&nbsp; There will only ever be one you!&nbsp; And importantly, respect the differences of others. Our world would be a drab, boring place if we all&nbsp; only whistled one tune.</p>

  <div class="abs photo-kneel" role="img" aria-label="Black and white photograph of a dancer kneeling on pointe with arm extended, dark fabric billowing behind"></div>
</section>

</body>
</html>
```